Card for invoking rights with police

Our criminal defense law firm is seeking proposals for a design for our card intended for clients to carry with them in their car. Upon being pulled over, they would hand this card to the officer.
Text for the back of the card:
"For Law Enforcement:"
"I will comply with lawful orders but respectfully decline any test or other requests without my attorney. I wish to remain silent, do not consent to searches, and request to speak with my attorney now.
The back of the card should prominently feature the text and the firm logo should be secondary.
Front
Must prominently feature contact info: 503-555-0182. Do not include attorney name, email, phone from the example file. This is intended to be generic for the firm and not tied to an individual lawyer.
Included for design reference: current business card, firm logo.
We intend to use trenvo.com to produce the cards.
Updates
The back of the card should prominently display the text regarding invocation of rights. Please title it "For Law Enforcement".
Target Market(s)
People who have been stopped by police
Contact Information for Business Card
see project description
Look and feel

```html
<!DOCTYPE html>
<html lang="en">
<head>
<meta charset="utf-8">
<title>Halvern Law Firm – Rights Card</title>
<link rel="stylesheet" href="https://fonts.googleapis.com/css2?family=Cinzel:wght@400;600&family=Open+Sans:wght@400;600&family=Barlow+Condensed:wght@400;500;600&display=swap">
<style>
  :root {
    --page-bg: #d6d6d6;
    --navy: #0b2e52;
    --navy-deep: #062849;
    --navy-light: #17406b;
    --green: #6f905c;
    --white: #ffffff;
    --ink: #14355a;
  }
  * { box-sizing: border-box; margin: 0; padding: 0; }
  html, body { width: 900px; height: 1200px; overflow: hidden; }
  body { background: var(--page-bg); position: relative; font-family: "Open Sans", sans-serif; }

  .card { position: absolute; left: 127px; width: 646px; height: 364px; overflow: hidden; }
  .card--back { top: 212px; background: var(--navy); color: var(--white); }
  .card--front { top: 625px; background: var(--white); color: var(--ink); }

  .card__texture {
    position: absolute; inset: 0;
    background: radial-gradient(ellipse at 78% 40%, var(--navy-light) 0%, var(--navy) 45%, var(--navy-deep) 100%);
  }

  .brand { position: absolute; display: flex; align-items: center; gap: 10px; font-family: "Cinzel", serif; font-weight: 400; white-space: nowrap; }
  .brand__mark { display: block; flex: none; }

  .card--back .brand { left: 0; right: 0; top: 36px; justify-content: center; font-size: 17px; letter-spacing: 3px; color: var(--white); }
  .card--back .brand__mark { width: 26px; height: 26px; background: var(--white); }

  .rights { position: absolute; left: 40px; right: 40px; top: 104px; text-align: center; font-family: "Barlow Condensed", sans-serif; }
  .rights__title { font-size: 34px; font-weight: 600; letter-spacing: 0.5px; margin-bottom: 16px; }
  .rights__rule { width: 80px; height: 2px; background: var(--green); margin: 0 auto 18px; }
  .rights__text { font-size: 20px; line-height: 29px; font-weight: 400; letter-spacing: 0.2px; text-wrap: balance; }

  .card--front .brand { left: 0; right: 0; top: 42px; justify-content: center; font-size: 22px; letter-spacing: 4px; color: var(--navy); }
  .card--front .brand__mark { width: 34px; height: 34px; background: var(--navy); }

  .call-pill {
    position: absolute; left: 133px; top: 118px; width: 380px; height: 88px; border-radius: 44px;
    background: var(--green); color: var(--white); display: flex; align-items: center; justify-content: center; gap: 18px;
  }
  .call-pill__label { font-size: 17px; font-weight: 600; line-height: 1.1; }
  .call-pill__number { font-size: 32px; font-weight: 600; letter-spacing: 2px; line-height: 1.15; }

  .web { position: absolute; left: 37px; bottom: 40px; display: flex; align-items: center; gap: 8px; font-size: 17px; letter-spacing: 0.6px; color: var(--ink); }
  .web svg { width: 15px; height: 15px; fill: var(--green); flex: none; }

  .address { position: absolute; right: 37px; bottom: 36px; text-align: right; font-size: 14.5px; line-height: 24px; font-style: normal; color: var(--ink); }
</style>
</head>
<body>

<section class="card card--back" aria-label="Card back">
  <div class="card__texture" role="img" aria-label="Navy background with fine flowing wave line pattern"></div>
  <div class="brand"><span class="brand__mark"></span>HALVERN LAW FIRM</div>
  <div class="rights">
    <h2 class="rights__title">For Law Enforcement:</h2>
    <div class="rights__rule"></div>
    <p class="rights__text">I will comply with lawful orders but respectfully decline any test or other requests without my attorney. I wish to remain silent, do not consent to searches, and request to speak with my attorney now.</p>
  </div>
</section>

<section class="card card--front" aria-label="Card front">
  <div class="brand"><span class="brand__mark"></span>HALVERN LAW FIRM</div>

  <div class="call-pill">
    <svg width="40" height="40" viewBox="0 0 24 24" fill="#fff" aria-hidden="true">
      <path d="M6.6 10.8a15 15 0 0 0 6.6 6.6l2.2-2.2a1 1 0 0 1 1-.25 11.4 11.4 0 0 0 3.6.57 1 1 0 0 1 1 1V20a1 1 0 0 1-1 1A17 17 0 0 1 3 4a1 1 0 0 1 1-1h3.5a1 1 0 0 1 1 1c0 1.25.2 2.45.57 3.57a1 1 0 0 1-.25 1z"/>
      <path d="M14 3a7 7 0 0 1 7 7h-1.6A5.4 5.4 0 0 0 14 4.6zm0 3.2a3.8 3.8 0 0 1 3.8 3.8h-1.6A2.2 2.2 0 0 0 14 7.8z"/>
    </svg>
    <div>
      <div class="call-pill__label">Call Now:</div>
      <div class="call-pill__number">503-555-0182</div>
    </div>
  </div>

  <div class="web">
    <svg viewBox="0 0 24 24" aria-hidden="true"><path d="M12 2a10 10 0 1 0 0 20 10 10 0 0 0 0-20zm-1 3c-2 1-3 3-2 5s3 1 3 3-2 2-1 4 3 2 4 1c-1 2-3 2-5 2a8 8 0 0 1 1-15z"/></svg>
    www.halvernlawfirm.com
  </div>

  <address class="address">
    2150 Cedar Point Way NE<br>
    Suite 210<br>
    Brookfield, WA 98104
  </address>
</section>

</body>
</html>
```